Letterhead Design Project

Looking for letterhead designs for Brastova Mining.

I am looking for a letterhead design in conjunction with a business card design. I have opened contests for both but ask that if you submit a letterhead design you also submit a business card design with a corresponding look/feel.

Brastova Mining is a B2B company that buys and sells large machinery tires within the coal mining industry. The design should the strong, crisp and masculine. I have uploaded the company logo and mock-up of the back of the company's business card.

Color scheme should be grey/green/black

Contact information to include:
Name: Dale Whitford
Title: Managing Director
Phone: 555-231-4097
Address: 1817 Pellam #3 Dallas, TX 75290
Email: Dale@Brastova.example
Updates

Project Deadline Extended
Reason: Looking for a more refined, elegant letterhead than what's been submitted as of yet. Here is a sample of what we're looking for: http://www.plumcrestgallery.example/letterhead-designs/ We will also be increasing the payment.

Industry/Entity Type

Coal Mining

```html
<!DOCTYPE html>
<html lang="en">
<head>
<meta charset="utf-8">
<title>Brastova Mining — Stationery</title>
<link href="https://fonts.googleapis.com/css2?family=Open+Sans:wght@400;600;700&display=swap" rel="stylesheet">
<style>
  :root {
    --canvas: #eeeeee;
    --paper: #ffffff;
    --slate: #6b6b6b;
    --ink: #4a4a4a;
    --green: #6cb33f;
    --white: #ffffff;
  }
  * { box-sizing: border-box; margin: 0; padding: 0; }
  html, body {
    width: 1200px; height: 800px; overflow: hidden;
    background: var(--canvas);
    font-family: "Open Sans", Arial, sans-serif;
    color: var(--ink);
  }
  .stationery { position: relative; width: 1200px; height: 800px; }

  .brand {
    display: inline-flex; align-items: center; gap: 5px;
    font-weight: 700; letter-spacing: 0.04em; text-transform: uppercase;
    white-space: nowrap; line-height: 1;
  }
  .brand-square { display: inline-block; background: var(--green); }

  /* Business card, front */
  .card-front {
    position: absolute; left: 296px; top: 131px;
    width: 93px; height: 152px; background: var(--paper);
  }
  .card-front-content {
    position: absolute; left: 93px; top: 0;
    width: 152px; height: 93px;
    transform-origin: top left; transform: rotate(90deg);
  }
  .card-divider {
    position: absolute; left: 0; right: 0; top: 48px;
    height: 1px; background: var(--slate);
  }
  .card-front .brand { position: absolute; left: 22px; top: 64px; font-size: 8px; color: var(--slate); }
  .card-front .brand-square { width: 7px; height: 7px; }
  .card-person { position: absolute; left: 28px; top: 30px; }
  .card-name { font-size: 8px; color: var(--slate); line-height: 1; }
  .card-title { font-size: 5px; color: var(--green); margin-top: 2px; }
  .card-contact {
    position: absolute; left: 28px; top: 5px;
    font-size: 4px; line-height: 6px; color: var(--ink);
  }

  /* Business card, back */
  .card-back {
    position: absolute; left: 296px; top: 346px;
    width: 100px; height: 181px; background: var(--slate);
  }
  .card-back-content {
    position: absolute; left: 100px; top: 0;
    width: 181px; height: 100px;
    transform-origin: top left; transform: rotate(90deg);
    display: flex; align-items: center; justify-content: center;
  }
  .card-back .brand { font-size: 10px; color: var(--white); }
  .card-back .brand-square { width: 8px; height: 8px; }

  /* Letterhead */
  .letterhead {
    position: absolute; left: 441px; top: 100px;
    width: 427px; height: 600px; background: var(--paper);
  }
  .letterhead-header { position: absolute; left: 0; right: 0; top: 36px; text-align: center; }
  .letterhead-header .brand { font-size: 19px; color: var(--slate); }
  .letterhead-header .brand-square { width: 14px; height: 14px; }
  .letterhead-contact { margin-top: 14px; font-size: 8px; line-height: 11px; color: var(--ink); }
  .letterhead-footer {
    position: absolute; left: 0; right: 0; bottom: 0; height: 21px;
    background: var(--slate);
    display: flex; align-items: center; justify-content: center;
  }
  .letterhead-footer .brand { font-size: 8px; color: var(--white); }
  .letterhead-footer .brand-square { width: 7px; height: 7px; }
</style>
</head>
<body>
<main class="stationery">

  <section class="card-front" aria-label="Business card front">
    <div class="card-front-content">
      <div class="card-contact">
        <p>Dale@Brastova.example</p>
        <p>555-231-4097</p>
        <p>1817 Pellam #3 Dallas, TX 75290</p>
      </div>
      <div class="card-person">
        <p class="card-name">Dale Whitford</p>
        <p class="card-title">Managing Director</p>
      </div>
      <div class="card-divider"></div>
      <div class="brand"><span class="brand-square"></span>Brastova Mining</div>
    </div>
  </section>

  <section class="card-back" aria-label="Business card back">
    <div class="card-back-content">
      <div class="brand"><span class="brand-square"></span>Brastova Mining</div>
    </div>
  </section>

  <section class="letterhead" aria-label="Letterhead">
    <header class="letterhead-header">
      <div class="brand"><span class="brand-square"></span>Brastova Mining</div>
      <div class="letterhead-contact">
        <p>555-231-4097</p>
        <p>1817 Pellam #3 Dallas, TX 75290</p>
      </div>
    </header>
    <footer class="letterhead-footer">
      <div class="brand"><span class="brand-square"></span>Brastova Mining</div>
    </footer>
  </section>

</main>
</body>
</html>
```